Kestrel Valley Alpine Riders Society needs a business card design

We need a business card design for our newly incorporated KVARS. We are helping the NZ Chinese community, as well as everyone else, to organise ski & snowboarding trips, training, and equipments. The design should be creative, energetic, young and vibrant.

Industry/Entity Type

Social Club

Contact Information for Business Card

Logo; Kestrel Valley Alpine Riders Society; Name: Oliver Brandt; Position: President; Address: 42 Marwick Rd, Epsom, Auckland 1051; Mobile: 020 7826 1957; Email: oliver@kvars-club.example; Web: www.kvars-club.example

Requirements
Must have
• 1, The text "Kestrel Valley Alpine Riders Society" should be put together with the supplied logo file to form a new complete logo combination.
• 2, Final design files should be in Adobe Illustrator format and all text must be editable.
Nice to have
• two or three colours

```html
<!DOCTYPE html>
<html lang="en">
<head>
<meta charset="utf-8">
<title>Kestrel Valley Alpine Riders Society – Business Card</title>
<link rel="stylesheet" href="https://fonts.googleapis.com/css2?family=Exo+2:wght@700&family=Open+Sans:wght@400;600&display=swap">
<style>
  :root {
    --backdrop: #3a3a3c;
    --card: #1d1d1f;
    --card-edge: #151516;
    --ink: #f4f4f4;
    --accent: #2aa7df;
    --foil: #b9bcc0;
    --rule: #e8e8e8;
  }
  * { margin: 0; padding: 0; box-sizing: border-box; }
  html, body {
    width: 1200px; height: 1000px; overflow: hidden;
    background: var(--backdrop);
  }
  .stage {
    width: 1200px; height: 1000px;
    display: flex; flex-direction: column; align-items: center; justify-content: center;
    gap: 40px;
  }
  .card {
    position: relative;
    width: 760px; height: 434px;
    background: var(--card);
    border: 1px solid var(--card-edge);
    box-shadow: 0 14px 30px rgba(0,0,0,0.45);
  }
  /* Front */
  .card-front {
    display: flex; flex-direction: column; align-items: center; justify-content: center;
    gap: 6px;
  }
  .wordmark-foil {
    font-family: "Exo 2", sans-serif; font-weight: 700;
    font-size: 78px; letter-spacing: 2px; line-height: 1;
    color: var(--foil);
  }
  .club-name {
    font-family: "Open Sans", sans-serif; font-weight: 600;
    font-size: 17px; letter-spacing: 3px; text-transform: uppercase;
    color: var(--foil);
  }
  /* Back */
  .identity {
    position: absolute; top: 170px; right: 460px;
    text-align: right;
  }
  .person-name {
    font-family: "Exo 2", sans-serif; font-weight: 700;
    font-size: 32px; letter-spacing: 1.5px; color: var(--ink);
    line-height: 1.05;
  }
  .person-role {
    font-family: "Open Sans", sans-serif; font-weight: 600;
    font-size: 24px; letter-spacing: 1px; color: var(--accent);
    line-height: 1.2;
  }
  .divider {
    position: absolute; left: 320px; top: 178px;
    width: 2px; height: 66px; background: var(--rule);
  }
  .contact-list {
    position: absolute; left: 340px; top: 168px;
    list-style: none;
    font-family: "Open Sans", sans-serif; font-size: 18px; color: var(--ink);
  }
  .contact-item { display: flex; align-items: center; gap: 14px; height: 28px; }
  .contact-icon { width: 16px; height: 16px; flex: none; fill: var(--accent); }
  .contact-item .highlight { color: var(--accent); }
  .footer {
    position: absolute; left: 40px; bottom: 40px;
    display: flex; align-items: center; gap: 22px;
  }
  .wordmark-small {
    font-family: "Exo 2", sans-serif; font-weight: 700;
    font-size: 28px; letter-spacing: 1px; color: var(--accent);
  }
  .address {
    font-family: "Open Sans", sans-serif; font-size: 20px; letter-spacing: 0.8px;
    color: var(--ink);
  }
</style>
</head>
<body>
<main class="stage">
  <section class="card card-front" aria-label="Card front">
    <div class="wordmark-foil">KVARS</div>
    <div class="club-name">Kestrel Valley Alpine Riders Society</div>
  </section>

  <section class="card card-back" aria-label="Card back">
    <div class="identity">
      <div class="person-name">OLIVER BRANDT</div>
      <div class="person-role">President</div>
    </div>
    <div class="divider"></div>
    <ul class="contact-list">
      <li class="contact-item">
        <svg class="contact-icon" viewBox="0 0 16 16" aria-hidden="true"><path d="M3.2 1.5l2.3-.4 1.4 3.2-1.5 1.2c.8 1.8 2.2 3.2 4 4l1.2-1.5 3.2 1.4-.4 2.3c-.2.8-.9 1.3-1.7 1.2C6.4 12.4 3.6 9.6 2 4.4c-.1-.8.4-1.6 1.2-2.9z"/></svg>
        <span>020 7826 1957</span>
      </li>
      <li class="contact-item">
        <svg class="contact-icon" viewBox="0 0 16 16" aria-hidden="true"><path d="M1 3h14v1.2L8 8.6 1 4.2z"/><path d="M1 5.6l7 4.4 7-4.4V13H1z"/></svg>
        <span>oliver@kvars-club.example</span>
      </li>
      <li class="contact-item">
        <svg class="contact-icon" viewBox="0 0 16 16" aria-hidden="true"><path d="M9.5 1a5.5 5.5 0 1 1-3.4 9.8L2.3 14.6 1.2 13.5 5 9.7A5.5 5.5 0 0 1 9.5 1zm0 1.8a3.7 3.7 0 1 0 0 7.4 3.7 3.7 0 0 0 0-7.4z"/></svg>
        <span>www.<span class="highlight">kvars-club</span>.example</span>
      </li>
    </ul>
    <div class="footer">
      <span class="wordmark-small">KVARS</span>
      <span class="address">- 42 Marwick Rd, Epsom, Auckland 1051</span>
    </div>
  </section>
</main>
</body>
</html>
```